This will be a design for publicity materials for an event:

DEBATE: That the NRC will harm Asia's growing digital economies

Date: 18 July 2013, 19:00-21:00
Venue: Function Room 6, Level 3, The Lorvane Crest, Kota Kinabalu, Malaysia
RSVP: to tobias@welmarch.example by 11 July 2013, limited free tickets available

- blurb begins -

The Meridian Harbour Compact offers a golden opportunity for Asian nations to reap the rich rewards of global trade - or else it poses a dire threat to their sovereignty that would allow foreign multinational corporations to rewrite national laws for their own benefit. Opinions about the merits of the Meridian Harbour Compact for Asia are polarised, making it difficult for ordinary citizens to separate fact from fiction. So what better topic for a debate, to clear the air and shed some light on this impenetrable and controversial subject?

Shoppers Guildwide, in partnership with Byteline Report East, is hosting a free public 3-on-3 parliamentary-style debate on the proposition "That the NRC will harm Asia's growing digital economies". Drawn from across the region's government, industry and NGO communities, the participants will attempt to convince the audience that the NRC is the best hope for stimulating growth and innovation in Asia's high-tech industries - or that it will hamstring those industries with inappropriate laws pushed by foreign interests. Who wins? The audience will decide.

- blurb ends -

We want to have a design in 4 formats to promote this online, but you can just do one format to respond to the brief, and the others can come after I select a winner. One of the formats should be suitable to be emailed, so you could do it either as a graphic, or else as an HTML page suitable for emailing. The second format should be a 430 x 130 banner. Third should be a 300 x 250 banner. Also one format in about 800x600 or similar that we can use as a presentation slide at the venue.
Updates

Just to clarify, you don't need to include the whole blurb text.  Particularly in the small formats, that would be impossible.  It is mainly included as background for you.

I apologise for not getting back to you with comments and feedback - I had to travel to India and don't have proper Internet access here. I will get back to you as soon as I can. 

Target Market(s)

Business people, NGOs, diplomats

Industry/Entity Type

Industry

Requirements
Must have
• Sponsors' logos are attached.
Nice to have
• In at least the larger formats, we need to have space to show the names of the debaters. But we don't have those names yet, so for now it should say something like "Debating teams announced soon", with the facility to change it later when we do have the names. I had thought about maybe using a stage with a curtain drawn for the "coming soon" variant, and the curtains drawn back to reveal the names for the final variant. But I leave this to you.
Should not have
• Prefer if you don't use stock photos of people.

```html
<!DOCTYPE html>
<html lang="en">
<head>
<meta charset="utf-8">
<title>Debate: That the NRC will harm Asia's growing Digital Economies</title>
<link rel="stylesheet" href="https://fonts.googleapis.com/css2?family=Open+Sans:ital,wght@0,300;0,400;0,700;1,700&family=Kalam:wght@400&display=swap">
<style>
  :root {
    --sky-top: #163f66;
    --sky-mid: #3a78a8;
    --horizon: #d3e4ef;
    --sea-mid: #5b93bf;
    --sea-deep: #1d4b78;
    --headline: #ffffff;
    --label-yellow: #f6e51b;
    --accent-blue: #2a9be0;
    --bubble-blue: #3aa6e8;
    --bubble-orange: #ff9a1c;
    --globe-light: #dfe9f1;
    --globe-mid: #9fbdd6;
    --ink: #101010;
  }
  * { box-sizing: border-box; margin: 0; padding: 0; }
  html, body { width: 1200px; height: 900px; overflow: hidden; }
  body { font-family: "Open Sans", Arial, sans-serif; background: var(--sky-top); }

  .poster {
    position: relative;
    width: 1200px;
    height: 900px;
    overflow: hidden;
    background: linear-gradient(180deg,
      var(--sky-top) 0%,
      var(--sky-mid) 30%,
      #8fb8d6 44%,
      var(--horizon) 51%,
      #a9c8df 55%,
      var(--sea-mid) 66%,
      var(--sea-deep) 100%);
  }

  .globe { position: absolute; left: 0; top: 0; }

  .event-label {
    position: absolute;
    top: 10px; left: 0; width: 100%;
    text-align: center;
    font-weight: 700;
    font-size: 31px;
    color: var(--label-yellow);
    letter-spacing: 0.5px;
  }

  .headline {
    position: absolute;
    top: 56px; left: 0; width: 100%;
    text-align: center;
    font-weight: 300;
    font-size: 58px;
    line-height: 74px;
    color: var(--headline);
    text-shadow: 0 2px 6px rgba(0,0,0,0.35);
  }

  .debate-art {
    position: absolute;
    left: 292px; top: 240px;
    width: 586px; height: 398px;
    border-radius: 40px;
    background: linear-gradient(100deg,
      rgba(58,166,232,0.85) 0%,
      rgba(58,166,232,0.7) 45%,
      rgba(255,154,28,0.75) 60%,
      rgba(255,154,28,0.85) 100%);
  }

  .argument {
    position: absolute;
    color: var(--headline);
  }
  .argument__mark {
    position: absolute;
    font-weight: 700;
    font-size: 90px;
    line-height: 1;
  }
  .argument__text {
    font-weight: 700;
    font-style: italic;
    font-size: 19px;
    line-height: 42px;
    text-align: center;
    text-shadow: 0 1px 3px rgba(0,0,0,0.3);
  }
  .argument--for { left: 22px; top: 298px; width: 250px; }
  .argument--for .argument__mark { left: 0; top: 0; }
  .argument--for .argument__text { margin-top: 52px; padding-left: 20px; }
  .argument--against { left: 900px; top: 298px; width: 290px; }
  .argument--against .argument__mark { left: 6px; top: 0; }
  .argument--against .argument__text { margin-top: 52px; }
  .argument .acronym { color: var(--accent-blue); }

  .sponsors {
    position: absolute;
    left: 22px; top: 800px;
    display: flex;
    gap: 26px;
    align-items: center;
  }
  .sponsor {
    display: flex;
    align-items: center;
    gap: 8px;
    font-weight: 700;
    font-size: 17px;
    line-height: 21px;
    color: var(--headline);
  }
  .sponsor__dot {
    width: 14px; height: 14px;
    background: var(--headline);
    flex: none;
  }

  .details {
    position: absolute;
    left: 740px; top: 790px;
    width: 446px;
    text-align: right;
    font-size: 16px;
    line-height: 22px;
    color: var(--ink);
  }
  .details strong { font-weight: 700; }
  .details__note {
    display: block;
    font-family: "Kalam", cursive;
    font-size: 20px;
    line-height: 22px;
  }
</style>
</head>
<body>
<main class="poster">
  <svg class="globe" width="1200" height="900" viewBox="0 0 1200 900" role="img" aria-label="Globe seen from space with silhouettes of business people standing along its curved top">
    <defs>
      <radialGradient id="globe-fill" cx="0.55" cy="0.1" r="0.7">
        <stop offset="0" stop-color="#dfe9f1"/>
        <stop offset="0.5" stop-color="#9fbdd6"/>
        <stop offset="1" stop-color="#4f7fa6"/>
      </radialGradient>
    </defs>
    <circle cx="1050" cy="1452" r="782" fill="url(#globe-fill)"/>
  </svg>

  <h2 class="event-label">DEBATE</h2>
  <h1 class="headline">That the NRC will harm Asia's growing<br>Digital Economies</h1>

  <section class="argument argument--for">
    <span class="argument__mark">“</span>
    <p class="argument__text">Is the <span class="acronym">NRC</span> the best hope<br>for stimulating Growth<br>and Innovation in Asia's<br>High-Tech industries?</p>
  </section>

  <div class="debate-art" role="img" aria-label="Illustration of a blue and an orange speech bubble facing each other with question and exclamation marks above"></div>

  <section class="argument argument--against">
    <span class="argument__mark">“</span>
    <p class="argument__text">Or Does it threaten their<br>Sovereignty by allowing<br>Multinational Corporations to<br>Rewrite National Laws in<br>their own Interests?</p>
  </section>

  <footer class="sponsors">
    <div class="sponsor"><span class="sponsor__dot"></span><span>Even Terms<br>eventerms.example</span></div>
    <div class="sponsor"><span class="sponsor__dot"></span><span>Byteline<br>Report East</span></div>
    <div class="sponsor"><span class="sponsor__dot"></span><span>Shoppers<br>Guildwide</span></div>
  </footer>

  <section class="details">
    <p><strong>Date:</strong> 18 July 2013, 19:00-21:00</p>
    <p><strong>Venue:</strong> Function Room 6, Level 3,</p>
    <p>The Lorvane Crest, Kota Kinabalu, Malaysia</p>
    <p><strong>RSVP:</strong> to tobias@welmarch.example by 11 July 2013</p>
    <span class="details__note">limited free tickets available</span>
  </section>
</main>
</body>
</html>
```